Fret Riff Haven WebSite

I am looking for a website design for FretRiffHaven.com. If you are unfamiliar with the term "guitar lick": a guitar lick is a simple piece of music that is used in an improvisation or solo. All of the famous guitarists that you probably have heard of (Toby Marsland, Neil Brampton, etc.) have their own set of unique licks. This is what defines their style. The "Dojo" in the site name refers to a karate dojo. Basically, like a person would master karate in a karate dojo, a guitarist can master guitar licks in the Fret Riff Haven. The purpose of FretRiffHaven is to show users very high quality videos (youtube) and music notation for a variety of licks. Many of the guitar licks on the site will be from famous guitarists. There will also be licks that are not from famous guitarists, that are just general licks in a particular style or genre.

Target Market(s)

Intermediate and above guitar players.

Industry/Entity Type

Youtube

Requirements
Must have
• 1) The look and feel of the site must be based on the logo that I have attached. First and foremost, this site must be FUN. The page should fit with the mood of the logo. The logo should be incorporated well into the header design. It would be nice to see the logo theme used throughout the same page in some creative and reasonable way.
• 2) There will be three main navigation tabs on the home page: Licks, JamTracks, and Blog. The Licks section will be broken into Licks by Artist, and licks by genre (eg. Jazz, Rock, Blues, Fusion, Heavy Metal, Country, etc.)
• 3) There needs to be 3 main sections on the Home Page: Lick of the Day, Recently Added Licks, and Featured Licks. These 3 sections must contain thumbnails of the videos, along with a text description.
Nice to have
• Use the character from the logo or the karate theme in some creative way on the page.

```html
<!DOCTYPE html>
<html lang="en">
<head>
<meta charset="utf-8">
<title>Fret Riff Haven</title>
<link rel="stylesheet" href="https://fonts.googleapis.com/css2?family=Arvo:wght@400;700&family=Open+Sans:ital,wght@0,400;0,600;0,700;1,400;1,600&display=swap">
<style>
:root{
  --red:#e8232b;
  --blue:#1e97d4;
  --ink:#1c1c1c;
  --text:#555;
  --grey-bg:#efefef;
  --white:#fff;
  --dark:#242424;
  --card:#1b1b1b;
  --hero-a:#0a4f86;
  --hero-b:#1d9ad6;
  --hero-c:#7fd1f2;
}
*{box-sizing:border-box;margin:0;padding:0}
html,body{width:1200px;height:3005px;overflow:hidden}
body{font-family:"Open Sans",Arial,sans-serif;color:var(--text);background:var(--white);position:relative}
.abs{position:absolute}
.slab{font-family:"Arvo",Georgia,serif}

/* Hero */
.hero{position:absolute;left:0;top:0;width:1200px;height:716px;
  background:radial-gradient(ellipse at 62% 40%,var(--hero-c) 0%,var(--hero-b) 35%,var(--hero-a) 100%);overflow:hidden}
.hero-photo{position:absolute;left:640px;top:0;width:560px;height:716px;
  background:radial-gradient(ellipse at 50% 45%,rgba(40,40,50,.55) 0%,rgba(30,30,40,.25) 40%,rgba(0,0,0,0) 70%)}
.navbar{position:absolute;left:0;top:84px;width:1200px;height:56px;background:#0b0b0b}
.nav{position:absolute;right:108px;top:84px;height:56px;display:flex;gap:54px;align-items:center;list-style:none}
.nav a{font-family:"Arvo",Georgia,serif;font-weight:700;font-size:17px;color:var(--white);text-decoration:none}
.nav .active a{color:var(--red)}
.brand{position:absolute;left:112px;top:96px;display:flex;align-items:center;gap:10px}
.brand-dot{width:34px;height:34px;border-radius:50%;background:var(--red)}
.brand-name{font-family:"Arvo",Georgia,serif;font-weight:700;font-size:24px;color:var(--white)}
.connect{position:absolute;right:52px;top:34px;display:flex;align-items:center;gap:7px;color:var(--ink);font-size:15px;font-weight:600}
.connect .soc{width:22px;height:22px;border-radius:3px;background:#3b5f9e}
.connect .soc.b{background:#3fa9e0}
.connect .soc.c{background:#c4302b}
.hero-title{position:absolute;left:112px;top:292px;font-family:"Arvo",Georgia,serif;font-weight:700;font-size:72px;color:var(--ink);letter-spacing:1px}
.hero-sub{position:absolute;left:140px;top:372px;font-style:italic;font-weight:600;font-size:25px;color:var(--red)}
.hero-list{position:absolute;left:112px;top:428px;list-style:none}
.hero-list li{display:flex;align-items:center;gap:12px;font-size:23px;color:var(--ink);height:40px}
.dots{position:absolute;left:118px;top:668px;display:flex;gap:6px}
.dots span{width:12px;height:12px;border-radius:50%;background:#222}
.dots span:first-child{background:var(--red)}

/* shared section pieces */
.heading{font-family:"Arvo",Georgia,serif;font-weight:700;font-size:34px;line-height:42px;color:var(--ink)}
.heading .red{color:var(--red)}
.heading .blue{color:var(--blue)}
.para{font-size:13px;line-height:20px;color:var(--text)}
.para p+p{margin-top:16px}

/* Lick of the day */
.lotd{position:absolute;left:0;top:716px;width:1200px;height:538px;background:var(--grey-bg)}
.btn{display:inline-block;background:var(--red);color:var(--white);font-family:"Arvo",Georgia,serif;font-size:13px;font-weight:700;padding:12px 22px;border-radius:3px}
.video{position:absolute;left:518px;top:66px;width:572px;height:414px;background:#111;overflow:hidden}
.video-frame{position:absolute;inset:0 0 60px 0;background:linear-gradient(135deg,#5b4530 0%,#2b2018 45%,#6a3a28 75%,#1a1410 100%)}
.controls{position:absolute;left:0;bottom:0;width:572px;height:60px;background:#141414;border-top:4px solid var(--red)}
.controls .time{position:absolute;left:80px;top:20px;font-size:11px;color:#ccc}

/* licks rows */
.row{position:absolute;left:0;width:1200px}
.arrows{position:absolute;right:110px;display:flex;gap:10px}
.arrows span{width:24px;height:24px;border-radius:50%;background:#111;display:flex;align-items:center;justify-content:center}
.arrows span+span{background:#555}
.card{position:absolute;width:212px;height:314px;background:var(--card);border-radius:3px;overflow:hidden}
.card .thumb{position:absolute;left:0;top:0;width:212px;height:234px}
.card .cap{position:absolute;left:12px;top:242px;display:flex;gap:7px;align-items:center;font-family:"Arvo",Georgia,serif;font-weight:700;font-size:12px;color:var(--red)}
.card .desc{position:absolute;left:12px;top:266px;font-size:12px;line-height:18px;color:#666}
.play{position:absolute;left:66px;top:72px}
.t1{background:linear-gradient(160deg,#7a3b20,#b8582c 50%,#3a1d12)}
.t2{background:linear-gradient(160deg,#4b3826,#c7b9a4 55%,#2a2018)}
.t3{background:linear-gradient(160deg,#2a1c3a,#8a3a6a 50%,#1a1226)}

/* blog */
.blog{position:absolute;left:0;top:2110px;width:1200px;height:542px;background:var(--grey-bg)}
.blog-title{position:absolute;left:0;top:30px;width:1200px;text-align:center;font-family:"Arvo",Georgia,serif;font-weight:700;font-size:28px;color:var(--ink)}
.post{position:absolute;width:480px;height:200px}
.post .img{position:absolute;left:0;top:0;width:146px;height:104px}
.post .body{position:absolute;left:162px;top:0;width:318px}
.post h3{font-family:"Arvo",Georgia,serif;font-weight:700;font-size:16px;line-height:20px;color:var(--red);margin-bottom:4px}
.post .para{font-size:12.5px;line-height:20px}
.post .para p+p{margin-top:14px}
.b1{background:linear-gradient(135deg,#1a1a1a,#5a5550 60%,#222)}
.b2{background:linear-gradient(135deg,#1b1f5a,#4a6ad0 50%,#14143a)}
.b3{background:linear-gradient(135deg,#5a2a0e,#e09030 50%,#2a1406)}
.b4{background:linear-gradient(135deg,#1f2a24,#4f6a50 55%,#121a16)}

/* footer */
.footer{position:absolute;left:0;top:2652px;width:1200px;height:296px;background:var(--dark);color:#bbb}
.f-head{position:absolute;top:30px;display:flex;align-items:center;gap:7px;font-size:15px;font-weight:600;color:var(--white);text-transform:uppercase}
.f-links{position:absolute;left:126px;top:72px;list-style:none;font-size:13px;line-height:20px;color:#aaa}
.f-social{position:absolute;left:130px;top:226px;display:flex;gap:22px}
.f-social span{width:22px;height:22px;border-radius:50%;background:#ddd}
.comment{position:absolute;left:376px;width:320px;height:60px}
.comment .avatar{position:absolute;left:0;top:0;width:50px;height:50px;background:#cfcfcf}
.comment .txt{position:absolute;left:66px;top:0;font-size:11.5px;line-height:17px;font-style:italic;color:#999}
.comment .when{color:var(--red)}
.nl-text{position:absolute;left:778px;top:64px;width:310px;font-size:12.5px;line-height:20px;color:#aaa}
.nl-input{position:absolute;left:778px;top:140px;width:310px;height:42px;border:1px solid #444;background:#222;color:#999;font-size:13px;padding:12px 14px}
.nl-btn{position:absolute;left:948px;top:190px;width:140px;height:42px;background:var(--red);color:var(--white);font-weight:700;font-size:16px;display:flex;align-items:center;justify-content:center;border-radius:2px}
.bottom{position:absolute;left:0;top:2948px;width:1200px;height:57px;background:var(--white);font-size:13px;color:#777}
.bottom .copy{position:absolute;left:112px;top:18px}
.bottom .legal{position:absolute;right:110px;top:18px}
</style>
</head>
<body>

<header class="hero">
  <div class="hero-photo" role="img" aria-label="Photo of a guitarist in a beanie leaping with a natural-finish bass guitar"></div>
  <div class="navbar"></div>
  <div class="brand"><span class="brand-dot"></span><span class="brand-name">FretRiffHaven</span></div>
  <div class="connect">Connect With Us: <span class="soc"></span><span class="soc b"></span><span class="soc c"></span></div>
  <ul class="nav">
    <li class="active"><a href="#">HOME</a></li>
    <li><a href="#">LICKS</a></li>
    <li><a href="#">JAMTRACKS</a></li>
    <li><a href="#">BLOG</a></li>
  </ul>
  <h1 class="hero-title">Jam Tracks</h1>
  <p class="hero-sub">High Quality Backing Tracks</p>
  <ul class="hero-list">
    <li><svg width="18" height="20" viewBox="0 0 18 20"><path d="M6 2 L16 0 V13" stroke="#e8232b" stroke-width="2.5" fill="none"/><circle cx="4" cy="15" r="4" fill="#e8232b"/><circle cx="13" cy="13" r="3.5" fill="#e8232b"/></svg>Many styles to choose from</li>
    <li><svg width="18" height="20" viewBox="0 0 18 20"><path d="M6 2 L16 0 V13" stroke="#e8232b" stroke-width="2.5" fill="none"/><circle cx="4" cy="15" r="4" fill="#e8232b"/><circle cx="13" cy="13" r="3.5" fill="#e8232b"/></svg>High quality mp3 format</li>
    <li><svg width="18" height="20" viewBox="0 0 18 20"><path d="M6 2 L16 0 V13" stroke="#e8232b" stroke-width="2.5" fill="none"/><circle cx="4" cy="15" r="4" fill="#e8232b"/><circle cx="13" cy="13" r="3.5" fill="#e8232b"/></svg>Instant Download</li>
  </ul>
  <div class="dots"><span></span><span></span><span></span></div>
</header>

<section class="lotd">
  <h2 class="heading abs" style="left:112px;top:76px">LICK<br><span class="red">OF THE DAY</span></h2>
  <div class="para abs" style="left:112px;top:180px;width:330px">
    <p>Lorem ipsum dolor sit amet, consectetur adipiscing elit, sed do eiusmod tempor incididunt ut labore et dolore magna aliqua.</p>
    <p>Ut enim ad minim veniam, quis nostrud exercitation ullamco laboris nisi ut aliquip ex ea commodo consequat sed do eiusmod tempor incididunt ut labore et dolore magna aliqua.</p>
    <p>Lorem ipsum dolor sit amet, consectetur adipiscing elit, sed do eiusmod tempor incididunt ut labore et dolore magna aliqua.</p>
  </div>
  <a class="btn abs" style="left:110px;top:428px">LEARN MORE</a>
  <div class="video">
    <div class="video-frame" role="img" aria-label="Video still of a guitarist performing live on stage"></div>
    <svg class="abs" style="left:216px;top:112px" width="140" height="140" viewBox="0 0 140 140"><circle cx="70" cy="70" r="62" fill="rgba(255,255,255,.15)" stroke="#fff" stroke-width="7"/><path d="M56 40 L100 70 L56 100 Z" fill="#fff"/></svg>
    <div class="controls">
      <svg class="abs" style="left:24px;top:20px" width="14" height="16"><rect x="1" y="1" width="4" height="14" fill="#fff"/><rect x="9" y="1" width="4" height="14" fill="#fff"/></svg>
      <span class="time">00:54:21 / 01:40:30</span>
      <svg class="abs" style="left:376px;top:18px" width="12" height="18"><path d="M4 2 L11 0 V12" stroke="#ccc" stroke-width="2" fill="none"/><circle cx="3" cy="14" r="3" fill="#ccc"/></svg>
      <div class="abs" style="left:400px;top:26px;width:60px;height:4px;background:#444"><div style="width:38px;height:4px;background:var(--red)"></div></div>
      <div class="abs" style="left:500px;top:0;width:1px;height:56px;background:#333"></div>
      <svg class="abs" style="left:528px;top:20px" width="16" height="16" viewBox="0 0 16 16" stroke="#fff" stroke-width="2" fill="none"><path d="M1 5V1h4M11 1h4v4M15 11v4h-4M5 15H1v-4"/></svg>
    </div>
  </div>
</section>

<section class="row" style="top:1254px;height:424px">
  <div class="arrows" style="top:14px">
    <span><svg width="10" height="10"><path d="M7 1 L3 5 L7 9" stroke="#fff" stroke-width="2" fill="none"/></svg></span>
    <span><svg width="10" height="10"><path d="M3 1 L7 5 L3 9" stroke="#fff" stroke-width="2" fill="none"/></svg></span>
  </div>
  <h2 class="heading abs" style="left:112px;top:70px">RECENTLY<br><span class="blue">ADDED LICKS</span></h2>
  <div class="para abs" style="left:112px;top:180px;width:290px">
    <p>Lorem ipsum dolor sit amet, consectetur adipiscing elit, sed do eiusmod tempor incididunt ut labore et dolore magna aliqua.</p>
    <p>Ut enim ad minim veniam, quis nostrud exercitation ullamco laboris nisi ut aliquip ex ea commodo consequat...</p>
  </div>
  <article class="card" style="left:432px;top:52px"><div class="thumb t1" role="img" aria-label="Photo of a guitarist in a patterned shirt playing"></div><svg class="play" width="80" height="80"><circle cx="40" cy="40" r="35" fill="rgba(255,255,255,.15)" stroke="#fff" stroke-width="5"/><path d="M32 22 L58 40 L32 58Z" fill="#fff"/></svg><div class="cap"><svg width="12" height="14"><path d="M4 2 L11 0 V10" stroke="#fff" stroke-width="2" fill="none"/><circle cx="3" cy="11" r="3" fill="#fff"/><circle cx="9" cy="10" r="2.5" fill="#fff"/></svg>TOBY MARSLAND ALBUM</div><p class="desc">Lorem ipsum dolor sit amet,<br>consectetur</p></article>
  <article class="card" style="left:654px;top:52px"><div class="thumb t2" role="img" aria-label="Photo of a guitarist in a white jacket playing"></div><svg class="play" width="80" height="80"><circle cx="40" cy="40" r="35" fill="rgba(255,255,255,.15)" stroke="#fff" stroke-width="5"/><path d="M32 22 L58 40 L32 58Z" fill="#fff"/></svg><div class="cap"><svg width="12" height="14"><path d="M4 2 L11 0 V10" stroke="#fff" stroke-width="2" fill="none"/><circle cx="3" cy="11" r="3" fill="#fff"/><circle cx="9" cy="10" r="2.5" fill="#fff"/></svg>TOBY MARSLAND ALBUM</div><p class="desc">Lorem ipsum dolor sit amet,<br>consectetur</p></article>
  <article class="card" style="left:876px;top:52px"><div class="thumb t3" role="img" aria-label="Photo of a guitarist under purple stage lights"></div><svg class="play" width="80" height="80"><circle cx="40" cy="40" r="35" fill="rgba(255,255,255,.15)" stroke="#fff" stroke-width="5"/><path d="M32 22 L58 40 L32 58Z" fill="#fff"/></svg><div class="cap"><svg width="12" height="14"><path d="M4 2 L11 0 V10" stroke="#fff" stroke-width="2" fill="none"/><circle cx="3" cy="11" r="3" fill="#fff"/><circle cx="9" cy="10" r="2.5" fill="#fff"/></svg>TOBY MARSLAND ALBUM</div><p class="desc">Lorem ipsum dolor sit amet,<br>consectetur</p></article>
  <div class="abs" style="left:60px;top:420px;width:1080px;height:1px;background:linear-gradient(90deg,transparent,#ddd 20%,#ddd 80%,transparent)"></div>
</section>

<section class="row" style="top:1690px;height:420px">
  <div class="arrows" style="top:16px">
    <span><svg width="10" height="10"><path d="M7 1 L3 5 L7 9" stroke="#fff" stroke-width="2" fill="none"/></svg></span>
    <span><svg width="10" height="10"><path d="M3 1 L7 5 L3 9" stroke="#fff" stroke-width="2" fill="none"/></svg></span>
  </div>
  <h2 class="heading abs" style="left:112px;top:72px">MOST<br><span class="blue">POPULAR LICKS</span></h2>
  <div class="para abs" style="left:112px;top:182px;width:290px">
    <p>Lorem ipsum dolor sit amet, consectetur adipiscing elit, sed do eiusmod tempor incididunt ut labore et dolore magna aliqua.</p>
    <p>Ut enim ad minim veniam, quis nostrud exercitation ullamco laboris nisi ut aliquip ex ea commodo consequat...</p>
  </div>
  <article class="card" style="left:432px;top:54px"><div class="thumb t1" role="img" aria-label="Photo of a guitarist in a patterned shirt playing"></div><svg class="play" width="80" height="80"><circle cx="40" cy="40" r="35" fill="rgba(255,255,255,.15)" stroke="#fff" stroke-width="5"/><path d="M32 22 L58 40 L32 58Z" fill="#fff"/></svg><div class="cap"><svg width="12" height="14"><path d="M4 2 L11 0 V10" stroke="#fff" stroke-width="2" fill="none"/><circle cx="3" cy="11" r="3" fill="#fff"/><circle cx="9" cy="10" r="2.5" fill="#fff"/></svg>TOBY MARSLAND ALBUM</div><p class="desc">Lorem ipsum dolor sit amet,<br>consectetur</p></article>
  <article class="card" style="left:654px;top:54px"><div class="thumb t2" role="img" aria-label="Photo of a guitarist in a white jacket playing"></div><svg class="play" width="80" height="80"><circle cx="40" cy="40" r="35" fill="rgba(255,255,255,.15)" stroke="#fff" stroke-width="5"/><path d="M32 22 L58 40 L32 58Z" fill="#fff"/></svg><div class="cap"><svg width="12" height="14"><path d="M4 2 L11 0 V10" stroke="#fff" stroke-width="2" fill="none"/><circle cx="3" cy="11" r="3" fill="#fff"/><circle cx="9" cy="10" r="2.5" fill="#fff"/></svg>TOBY MARSLAND ALBUM</div><p class="desc">Lorem ipsum dolor sit amet,<br>consectetur</p></article>
  <article class="card" style="left:876px;top:54px"><div class="thumb t3" role="img" aria-label="Photo of a guitarist under purple stage lights"></div><svg class="play" width="80" height="80"><circle cx="40" cy="40" r="35" fill="rgba(255,255,255,.15)" stroke="#fff" stroke-width="5"/><path d="M32 22 L58 40 L32 58Z" fill="#fff"/></svg><div class="cap"><svg width="12" height="14"><path d="M4 2 L11 0 V10" stroke="#fff" stroke-width="2" fill="none"/><circle cx="3" cy="11" r="3" fill="#fff"/><circle cx="9" cy="10" r="2.5" fill="#fff"/></svg>TOBY MARSLAND ALBUM</div><p class="desc">Lorem ipsum dolor sit amet,<br>consectetur</p></article>
</section>

<section class="blog">
  <h2 class="blog-title">OUR BLOG</h2>
  <article class="post" style="left:110px;top:124px"><div class="img b1" role="img" aria-label="Photo of a guitarist in a dark jacket"></div><div class="body"><h3>Lorem Ipsum Dolor Sit Amet Consect-etur Adipisicing Elit</h3><div class="para"><p>Lorem ipsum dolor sit amet, consectetur adipiscing elit, sed do eiusmod tempor incididunt ut labore et dolore magna aliqua.</p><p>Ut enim ad minim veniam, quis nostrud exercitation ullamco laboris nisi ut aliquip ex ea commodo consequat...</p></div></div></article>
  <article class="post" style="left:618px;top:124px"><div class="img b2" role="img" aria-label="Photo of a guitarist on a blue-lit stage"></div><div class="body"><h3>Lorem Ipsum Dolor Sit Amet Consect-etur Adipisicing Elit</h3><div class="para"><p>Lorem ipsum dolor sit amet, consectetur adipiscing elit, sed do eiusmod tempor incididunt ut labore et dolore magna aliqua.</p><p>Ut enim ad minim veniam, quis nostrud exercitation ullamco laboris nisi ut aliquip ex ea commodo consequat...</p></div></div></article>
  <article class="post" style="left:110px;top:336px"><div class="img b3" role="img" aria-label="Photo of an electric guitar in warm sunset light"></div><div class="body"><h3>Lorem Ipsum Dolor Sit Amet Consect-etur Adipisicing Elit</h3><div class="para"><p>Lorem ipsum dolor sit amet, consectetur adipiscing elit, sed do eiusmod tempor incididunt ut labore et dolore magna aliqua.</p><p>Ut enim ad minim veniam, quis nostrud exercitation ullamco laboris nisi ut aliquip ex ea commodo consequat...</p></div></div></article>
  <article class="post" style="left:618px;top:336px"><div class="img b4" role="img" aria-label="Photo of a guitarist playing on a dim stage"></div><div class="body"><h3>Lorem Ipsum Dolor Sit Amet Consect-etur Adipisicing Elit</h3><div class="para"><p>Lorem ipsum dolor sit amet, consectetur adipiscing elit, sed do eiusmod tempor incididunt ut labore et dolore magna aliqua.</p><p>Ut enim ad minim veniam, quis nostrud exercitation ullamco laboris nisi ut aliquip ex ea commodo consequat...</p></div></div></article>
</section>

<footer class="footer">
  <div class="f-head" style="left:110px"><svg width="10" height="16"><path d="M7 0 L1 9 H5 L3 16 L9 6 H5 Z" fill="#fff"/></svg>Quick Links</div>
  <ul class="f-links"><li>Home</li><li>About Us</li><li>Licks</li><li>jamtracks</li><li>Blog</li><li>Contact Us</li></ul>
  <div class="f-social"><span></span><span></span><span></span><span></span><span></span></div>

  <div class="f-head" style="left:376px"><svg width="14" height="14"><circle cx="7" cy="4" r="3.5" fill="#fff"/><path d="M0 14 C0 8 14 8 14 14Z" fill="#fff"/></svg>Customer Comments</div>
  <div class="comment" style="top:70px"><div class="avatar" role="img" aria-label="Default user avatar"></div><p class="txt"><span class="when">About 14 days ago</span><br>Lorem ipsum dolor sit amet consectetur adipiscing elit, Sed do euismod tempor incidunt ut labore et dolore magna aliqua..</p></div>
  <div class="comment" style="top:152px"><div class="avatar" role="img" aria-label="Default user avatar"></div><p class="txt"><span class="when">About 14 days ago</span><br>Lorem ipsum dolor sit amet consectetur adipiscing elit, Sed do euismod tempor incidunt ut labore et dolore magna aliqua..</p></div>

  <div class="f-head" style="left:778px"><svg width="16" height="12"><rect x="1" y="1" width="14" height="10" fill="none" stroke="#fff" stroke-width="1.6"/><path d="M1 1 L8 7 L15 1" fill="none" stroke="#fff" stroke-width="1.6"/></svg>Newsletter</div>
  <p class="nl-text">Lorem ipsum dolor sit amet consectetur adipiscing elit, Sed do euismod tempor incidunt ut labore et dolore magna aliqua...</p>
  <div class="nl-input">E-mail</div>
  <div class="nl-btn">SUBMIT HERE</div>
</footer>

<div class="bottom">
  <span class="copy">Copyrights ©2015 FretRiffHaven.com - All Rights reserved</span>
  <span class="legal">Privacy Policy &nbsp;|&nbsp; Terms Of Uses</span>
</div>

</body>
</html>
```